Business Name "Kindred Stillness", Let your body do the talking through muscle testing. Tired of telli

There are 2 of us. We want the same basic card but different names and contact details. I will do my named one first and will confer with my business partner for this. I gather we then can get others printed with her name on it in the future. First things first.
Statement is "providing body/mind healing alternatives".
Lindenfall Healing is the modality. This is an energy healing technique, which uses muscle testing. The progammes treat the body/mind as a computer. The practitioner establishes the current need of the body with the muslce test which is at the wrist, and relays the correction by first defraging and deleting stuck patterns, blockages and imbalances. Replacing that which is no longer required or that which is causing discomfort within the body/mind, with positive affirmation, energy flow and balance. Specific programmes are used for the specific needs. The programmes incorporate the meridians, chakras - the energies of the body - and emotions. Also provides vibrational infusions of vitamins, mineral, cell salts, bach flowers etc where the body has indicated there is imbalance. The body asks for what it needs for optimal function. It is client driven, the practitioner is just the vessel/pathway for relaying or facilitating the changes required.
I need a logo, and format. Card to be clear, bold, not 'fluffy'. Any colour that indicates healing and wellbeing.
I want the business name and statement to be in English and Maori.
To have my name and mobile number.
At this stage we do not have a permanent clinic address and will get a website in the future.
The card to indicate open to all people not just for those seeking the 'lightworkers' way.

Target Market(s)

Anybody who is willing can receive this therapy. Even babies in utero, surrogates and distant healing.

Industry/Entity Type

Clinic

Font styles to use
Sans Serif

Colors
f0edf5
6b449b
9bcb3c

Requirements
Must have
• Logo (I do not have one or any idea)
The following words to be written on it
'Kindred Still-Ness'
'providing body/mind healing alternatives'
'Lindenfall Healing'
My name
and my contact details
'Kindred Stillness' and 'providing body/mind healing alternatives' to be written in italics or smaller print in MAORI

Nice to have
• Simple bold logo that has an eye catch appeal
Could use the name of business incorporated in the logo
White background is best
Clear crisp colours - 2 or 3 main colours
Should not have
• Black background
Too cramped
Too much detail

```html
<!DOCTYPE html>
<html lang="en">
<head>
<meta charset="utf-8">
<title>Kindred Stillness – Business Card</title>
<link href="https://fonts.googleapis.com/css2?family=Pathway+Gothic+One&family=Parisienne&family=Italianno&family=Arimo&display=swap" rel="stylesheet">
<style>
  :root {
    --bg-cyan: #82f7dc;
    --bg-green: #7ffc22;
    --motif: #9af06a;
    --ink: #1a3a02;
    --ink-dark: #0f2400;
  }
  html, body {
    margin: 0;
    padding: 0;
    width: 1200px;
    height: 637px;
    overflow: hidden;
    background: #ffffff;
  }
  .card {
    display: block;
    width: 1200px;
    height: 637px;
  }
  .brand-name { font-family: "Pathway Gothic One", "Arial Narrow", sans-serif; font-size: 212px; fill: var(--ink); }
  .tagline { font-family: "Pathway Gothic One", "Arial Narrow", sans-serif; font-size: 38px; fill: var(--ink); }
  .maori-name { font-family: "Parisienne", cursive; font-size: 118px; fill: var(--ink); }
  .modality { font-family: "Pathway Gothic One", "Arial Narrow", sans-serif; font-size: 46px; fill: var(--ink); }
  .modality-rule { stroke: var(--ink); stroke-width: 2; }
  .practitioner { font-family: "Italianno", cursive; font-size: 92px; fill: var(--ink-dark); }
  .phone { font-family: "Pathway Gothic One", "Arial Narrow", sans-serif; font-size: 40px; fill: var(--ink-dark); }
  .email { font-family: "Arimo", Arial, sans-serif; font-size: 33px; fill: var(--ink-dark); }
</style>
</head>
<body>
<svg class="card" viewBox="0 0 1200 637" xmlns="http://www.w3.org/2000/svg">
  <defs>
    <linearGradient id="card-bg" x1="0" y1="1" x2="0.75" y2="0">
      <stop offset="0" stop-color="var(--bg-cyan)"/>
      <stop offset="0.55" stop-color="var(--bg-green)"/>
      <stop offset="1" stop-color="var(--bg-green)"/>
    </linearGradient>
  </defs>

  <rect class="background" width="1200" height="637" fill="url(#card-bg)"/>

  <ellipse class="motif" cx="612" cy="318" rx="308" ry="262" fill="var(--motif)" opacity="0.75"
           role="img" aria-label="Circular swirling leaf pattern in soft greens"/>

  <text class="brand-name" x="54" y="212" textLength="600" lengthAdjust="spacingAndGlyphs">Kindred Stillness</text>
  <text class="tagline" x="53" y="253" textLength="552" lengthAdjust="spacingAndGlyphs">Providing body/mind healing alternatives</text>

  <text class="maori-name" x="60" y="362" textLength="588" lengthAdjust="spacingAndGlyphs">Oranga</text>

  <text class="modality" x="84" y="482" textLength="270" lengthAdjust="spacingAndGlyphs">Lindenfall Healing</text>
  <line class="modality-rule" x1="73" y1="493" x2="380" y2="493"/>

  <text class="practitioner" x="693" y="456" textLength="467" lengthAdjust="spacingAndGlyphs">Mara Tennwick</text>
  <text class="phone" x="805" y="535" textLength="251" lengthAdjust="spacingAndGlyphs">Tel - 027 5140283</text>
  <text class="email" x="726" y="602" textLength="404" lengthAdjust="spacingAndGlyphs">hello@kindredstillness.nz</text>
</svg>
</body>
</html>
```